Web Design Project for a new download application :-)

We need a website design and a logo design for a new website and desktop application.
The Website will be www.Fetchora.com
The installed application will be: Fetchora

Fetchora is a desktop application that searches and finds all kind of Media files (Movies, Games, Songs, software, etc..)
Fetchora will also manage the download process for the selected files.
Fetchora automates the whole search and download process.

User Flow:
users will initially visit the website.
user will download the application from the website
user will install the application on his computer.
user will run and use the application.

What makes our software special:
-Great search engine for searching media files.
-Very high speed downloads. maximum speeds.
-Allow used to Search by: file type, size, date, format
-Pause and resume downloads
-Get any file you want instantly.
-Unlimited Downloads.

We will need:
Logo
WebSite Design
Icons for the desktop application.

we need only PSDs - no codded pages are needed !

Design to the following screen Size & resolution: 1024 x 768

Target Market(s)

movies and music lovers.
users who download movies, games, softwares, music etc...

Industry/Entity Type

Software

Requirements
Must have
• must have download button

Files

```html
<!DOCTYPE html>
<html lang="en">
<head>
<meta charset="utf-8">
<title>Fetchora – media search engine</title>
<link rel="stylesheet" href="https://fonts.googleapis.com/css2?family=PT+Sans:wght@400;700&display=swap">
<style>
:root{
  --ink:#6f6f6f;
  --ink-dark:#555;
  --ink-light:#9a9a9a;
  --green:#5cb22d;
  --green-dark:#3f8f1c;
  --green-light:#86d04f;
  --panel:#f4f4f4;
  --rule:#d6d6d6;
  --arrow:#7a7a7a;
  --tile-top:#fafafa;
  --tile-bottom:#dedede;
}
*{box-sizing:border-box;margin:0;padding:0}
html,body{width:1200px;height:623px;overflow:hidden;background:#fff}
body{font-family:"PT Sans",Arial,sans-serif;color:var(--ink);position:relative}
.page{position:absolute;left:25px;top:25px;width:1153px;height:575px;background:#fff;overflow:hidden}
.header{position:absolute;left:0;top:0;width:100%;height:110px;background:linear-gradient(#dcdcdc,#f1f1f1 70%,#fff)}
.brand{position:absolute;left:47px;top:14px}
.brand-name{font-size:56px;font-weight:700;color:var(--ink);line-height:1;letter-spacing:-1px}
.brand-tag{font-size:21px;color:var(--ink);margin-left:40px;line-height:1}
.search{position:absolute;left:696px;top:13px;width:187px;height:19px;border:1px solid #cfcfcf;background:#fff;font-size:12px;color:var(--ink);padding:1px 6px}
.account{position:absolute;left:890px;top:14px;font-size:12px;color:var(--ink)}
.account span{color:#aaa}
.btn{background:linear-gradient(var(--green-light),var(--green) 55%,var(--green-dark));color:#fff;text-align:center;border:1px solid var(--green-dark)}
.app-btn{position:absolute;left:1014px;top:13px;width:127px;height:19px;font-size:12px;line-height:17px;border-radius:2px}
.home{position:absolute;left:524px;top:60px}
.nav{position:absolute;left:565px;top:63px;display:flex;gap:4px;list-style:none}
.nav li{height:25px;font-size:14px;line-height:23px;border-radius:3px 3px 0 0}
.hero{position:absolute;left:0;top:0}
.tile{position:absolute;width:78px;height:79px;border:1px solid #bdbdbd;border-radius:8px;background:linear-gradient(var(--tile-top),var(--tile-bottom))}
.tile .art{position:absolute;left:18px;top:18px;width:42px;height:42px;border-radius:8px}
.label{position:absolute;width:110px;text-align:center;font-size:11px;color:var(--ink-dark)}
.intro{position:absolute;left:817px;top:123px;width:320px}
.intro h1{font-size:36px;font-weight:700;color:#7a7a7a;line-height:1;letter-spacing:-.5px;margin-bottom:9px}
.intro p{font-size:13px;line-height:16.6px;color:var(--ink);margin-bottom:16px}
.intro b{color:var(--ink-dark)}
.get-now{position:absolute;left:817px;top:409px;width:239px;height:34px;font-size:20px;line-height:32px;border-radius:2px}
.footer{position:absolute;left:0;top:472px;width:100%;height:103px;background:linear-gradient(#fff,#ececec)}
.col{position:absolute;top:10px;font-size:11px}
.col h2{font-size:11px;font-weight:700;color:var(--green);margin-bottom:6px}
.col ul{list-style:none;line-height:13.3px;color:var(--ink)}
.divider{position:absolute;top:14px;width:1px;height:80px;background:var(--rule)}
.count{font-size:29px;color:var(--ink);margin-top:4px}
.social{display:flex;gap:6px}
.social span{width:25px;height:25px;border-radius:2px}
.legal{position:absolute;left:611px;top:38px;display:flex;align-items:center;gap:8px;font-size:9.5px;color:var(--ink-dark)}
.legal strong{font-size:20px;font-weight:700;color:var(--ink)}
.legal a{color:var(--green);text-decoration:none}
</style>
</head>
<body>
<div class="page">
  <header class="header">
    <div class="brand">
      <div class="brand-name">Fetchora</div>
      <div class="brand-tag">media search engine</div>
    </div>
    <div class="search">Search media . . .</div>
    <div class="account">Sign in <span>| Register | Help</span></div>
    <div class="btn app-btn">get Fetchora App</div>
    <svg class="home" width="30" height="28" viewBox="0 0 30 28" aria-label="Home">
      <path d="M2 14 L15 3 L28 14 M6 11 V26 H24 V11" fill="none" stroke="#c4c4c4" stroke-width="3"/>
      <rect x="12" y="17" width="6" height="9" fill="#c4c4c4"/>
    </svg>
    <ul class="nav">
      <li class="btn" style="width:113px">Categories</li>
      <li class="btn" style="width:111px">Browse media</li>
      <li class="btn" style="width:113px">New media</li>
      <li class="btn" style="width:113px">News</li>
      <li class="btn" style="width:112px">About us</li>
    </ul>
  </header>

  <section class="hero">
    <div role="img" aria-label="Blue globe with a magnifying glass" style="position:absolute;left:30px;top:223px;width:122px;height:122px;border-radius:50%;background:radial-gradient(circle at 40% 35%,#9fd0f5,#2a7fd0 55%,#154f9a)"></div>

    <svg width="1153" height="575" style="position:absolute;left:0;top:0" aria-hidden="true">
      <g fill="none" stroke="var(--arrow)" stroke-width="6">
        <path d="M233 183 H193 V385 H233"/>
        <path d="M233 285 H163"/>
        <path d="M530 183 H571 V385 H530"/>
        <path d="M530 285 H603"/>
      </g>
      <g fill="var(--arrow)">
        <path d="M243 183 l-14 -10 v20 z"/>
        <path d="M243 285 l-14 -10 v20 z"/>
        <path d="M243 385 l-14 -10 v20 z"/>
        <path d="M155 285 l14 -10 v20 z"/>
        <path d="M522 183 l14 -10 v20 z"/>
        <path d="M522 285 l14 -10 v20 z"/>
        <path d="M522 385 l14 -10 v20 z"/>
        <path d="M609 285 l-14 -10 v20 z"/>
      </g>
      <rect x="615" y="217" width="135" height="139" rx="18" fill="url(#boxfill)" stroke="#b8b8b8" stroke-width="2"/>
      <defs>
        <linearGradient id="boxfill" x1="0" y1="0" x2="0" y2="1">
          <stop offset="0" stop-color="#f2f2f2"/><stop offset="1" stop-color="#cfcfcf"/>
        </linearGradient>
      </defs>
      <text x="682" y="292" text-anchor="middle" font-family="PT Sans, sans-serif" font-weight="700" font-size="20" fill="#6f6f6f">Fetchora</text>
    </svg>

    <div class="tile" style="left:249px;top:133px"><div class="art" role="img" aria-label="Speaker icon" style="background:#8a8a8a"></div></div>
    <div class="tile" style="left:343px;top:133px"><div class="art" role="img" aria-label="Film strip icon" style="background:#3a3a3a"></div></div>
    <div class="tile" style="left:438px;top:133px"><div class="art" role="img" aria-label="Photo icon" style="background:#4a9ad6"></div></div>
    <div class="tile" style="left:249px;top:237px"><div class="art" role="img" aria-label="Music note icon" style="background:#2a86d6"></div></div>
    <div class="tile" style="left:343px;top:237px"><div class="art" role="img" aria-label="Paint palette icon" style="background:#e0a24a"></div></div>
    <div class="tile" style="left:438px;top:237px"><div class="art" role="img" aria-label="Television icon" style="background:#b86a1e"></div></div>
    <div class="tile" style="left:249px;top:341px"><div class="art" role="img" aria-label="Puzzle piece icon" style="background:#9a5bb8"></div></div>
    <div class="tile" style="left:343px;top:341px"><div class="art" role="img" aria-label="Terminal window icon" style="background:#2e2e2e"></div></div>
    <div class="tile" style="left:438px;top:341px"><div class="art" role="img" aria-label="Folder icon" style="background:#e8c85a"></div></div>

    <div class="label" style="left:233px;top:216px">music</div>
    <div class="label" style="left:327px;top:216px">videos</div>
    <div class="label" style="left:422px;top:216px">photos</div>
    <div class="label" style="left:233px;top:320px">sounds</div>
    <div class="label" style="left:327px;top:320px">wallpapers</div>
    <div class="label" style="left:422px;top:320px">tw shovs</div>
    <div class="label" style="left:233px;top:423px">applications</div>
    <div class="label" style="left:327px;top:424px">softwares</div>
    <div class="label" style="left:422px;top:423px">tipe of files</div>
  </section>

  <section class="intro">
    <h1>Welcome to Fetchora</h1>
    <p><b>Fetchora</b> is the largest media search engine libery<br>where you can search and download<br>any of your favorite media contents.</p>
    <p><b>FAST</b>, <b>RELIABLE</b> and <b>SECURE . . .</b><br><b>Fetchora</b> will make your search and download<br>an interesting and entertaining<br>and most importantly free.</p>
    <p>So hurry up and download <b>Fetchora</b> witch gives you<br>the freedom to choose directly to your computer<br>mobile phones and other multi tasks devices.<br><b>FREEDOM IS YOUR CHOICE !</b></p>
  </section>
  <div class="btn get-now">get Fetchora Now !</div>

  <footer class="footer">
    <div class="col" style="left:14px">
      <h2>Looking for a . . .</h2>
      <ul><li>Music</li><li>Movies</li><li>Wallpapers</li><li>Games</li><li>Softwares . . .</li></ul>
    </div>
    <div class="divider" style="left:128px"></div>
    <div class="col" style="left:168px">
      <h2>About . . .</h2>
      <ul><li>About us</li><li>How it Works</li><li>Contact us</li><li>Help</li><li>Blog</li></ul>
    </div>
    <div class="divider" style="left:258px"></div>
    <div class="col" style="left:288px">
      <h2>Recent media storage . . .</h2>
      <div class="count">298,653</div>
    </div>
    <div class="divider" style="left:452px"></div>
    <div class="col" style="left:482px">
      <h2>Follow us . . .</h2>
      <div class="social" aria-label="Social links">
        <span style="background:#3b5a9a"></span>
        <span style="background:#5fb6de"></span>
        <span style="background:#e8742a"></span>
      </div>
    </div>
    <div class="legal">
      <strong>Fetchora</strong>
      <span>Copyright © 2011 Fetchora. Use of this website constitutes acceptance of our <a>User Agreement</a> and <a>Privacy Policy</a>.</span>
    </div>
  </footer>
</div>
</body>
</html>
```